Business Card for Orvane Parts Wholesale supplier

Hi There! I need a new business card for our company. We are specialized in selling Orvane parts, mostly we sell new LCD screens for Telvox and Slatrons. I would like to see that back in the design.

You can find the colors and logo's on our website: www.dorvak-example.nl

Industry/Entity Type

Business

Contact Information for Business Card

My Details:
Lars Vintorp

Phone: 0031612873406
E-mail: Lars@dorvak-example.nl

Slogan: "Because Quality Matters"

Font styles to use
Sans Serif

Colors

Designer to choose colors to be used in the design.

Requirements
Must have
• A Black backside with the Dorvak logo on it. The front side should be clean with only my contact details.
• But I'm also open for something really different or awesome!
Nice to have
• Remember that we are in the parts & repairing industry, So i'll be handing those business cards mainly to repair companies. Maybe you can do something with that thought :)

```html
<!DOCTYPE html>
<html lang="en">
<head>
<meta charset="UTF-8">
<title>Dorvak Business Card</title>
<link href="https://fonts.googleapis.com/css2?family=Arimo:wght@400;700&family=Libre+Baskerville:ital@1&display=swap" rel="stylesheet">
<style>
  :root {
    --bg-light: #ececec;
    --bg-dark: #d9dada;
    --card-black: #0d0d0d;
    --card-white: #ffffff;
    --ink: #1f1f1f;
    --ink-soft: #3a3a3a;
    --accent: #e8641c;
    --rule: #2a2a2a;
  }
  * { margin: 0; padding: 0; box-sizing: border-box; }
  html, body { width: 1200px; height: 800px; overflow: hidden; }
  body {
    background: radial-gradient(ellipse at center, var(--bg-light) 0%, var(--bg-dark) 100%);
    font-family: "Arimo", Arial, sans-serif;
    position: relative;
  }
  .card {
    position: absolute;
    top: 250px;
    width: 525px;
    height: 300px;
    border-radius: 26px;
    box-shadow: 0 6px 18px rgba(0,0,0,0.12);
  }
  /* Back side */
  .card-back {
    left: 50px;
    background: var(--card-black);
    display: flex;
    align-items: center;
    justify-content: center;
  }
  .brand-back {
    display: flex;
    align-items: center;
    gap: 16px;
    color: #ffffff;
  }
  .brand-mark-back {
    width: 46px;
    height: 46px;
    border-radius: 50%;
    background: #ffffff;
  }
  .brand-name-back {
    font-weight: 700;
    font-size: 62px;
    letter-spacing: 1px;
    line-height: 1;
  }
  /* Front side */
  .card-front {
    left: 625px;
    background: var(--card-white);
    display: flex;
    align-items: center;
    padding: 0 36px 0 38px;
  }
  .front-brand {
    width: 200px;
  }
  .brand-front {
    display: flex;
    align-items: center;
    gap: 8px;
    padding-bottom: 6px;
    border-bottom: 1px solid var(--rule);
  }
  .brand-mark-front {
    width: 26px;
    height: 26px;
    border-radius: 50%;
    background: var(--accent);
  }
  .brand-name-front {
    font-weight: 700;
    font-size: 36px;
    color: var(--ink);
    line-height: 1;
    letter-spacing: 0.5px;
  }
  .slogan {
    font-family: "Libre Baskerville", "Times New Roman", serif;
    font-style: italic;
    font-size: 13px;
    color: var(--ink-soft);
    margin-top: 6px;
  }
  .divider {
    width: 2px;
    height: 120px;
    background: var(--rule);
    margin: 0 30px 0 18px;
  }
  .contact {
    flex: 1;
    color: var(--ink);
  }
  .contact-name {
    font-weight: 700;
    font-size: 16px;
    text-align: center;
    margin-bottom: 16px;
  }
  .contact-list { list-style: none; }
  .contact-item {
    display: flex;
    align-items: center;
    gap: 10px;
    font-size: 14px;
    margin-bottom: 5px;
  }
  .contact-icon { width: 16px; height: 16px; flex: none; }
</style>
</head>
<body>
  <section class="card card-back" aria-label="Card back">
    <div class="brand-back">
      <span class="brand-mark-back"></span>
      <span class="brand-name-back">dorvak</span>
    </div>
  </section>

  <section class="card card-front" aria-label="Card front">
    <div class="front-brand">
      <div class="brand-front">
        <span class="brand-mark-front"></span>
        <span class="brand-name-front">dorvak</span>
      </div>
      <p class="slogan">Because Quality Matters</p>
    </div>
    <div class="divider"></div>
    <div class="contact">
      <p class="contact-name">Lars Vintorp</p>
      <ul class="contact-list">
        <li class="contact-item">
          <svg class="contact-icon" viewBox="0 0 16 16" aria-hidden="true">
            <circle cx="8" cy="8" r="7" fill="none" stroke="#1f1f1f" stroke-width="1.3"/>
            <path d="M5.5 4.5l1.3 1.3-.8 1c.5 1.1 1.2 1.8 2.3 2.3l1-.8 1.3 1.3-.9 1.2c-2.5-.4-4.5-2.4-4.9-4.9z" fill="#1f1f1f"/>
          </svg>
          <span>0031612873406</span>
        </li>
        <li class="contact-item">
          <svg class="contact-icon" viewBox="0 0 16 16" aria-hidden="true">
            <text x="8" y="12.5" text-anchor="middle" font-family="Arimo, Arial, sans-serif" font-weight="700" font-size="14" fill="#1f1f1f">@</text>
          </svg>
          <span>lars@dorvak-example.nl</span>
        </li>
        <li class="contact-item">
          <svg class="contact-icon" viewBox="0 0 16 16" aria-hidden="true">
            <g fill="none" stroke="#1f1f1f" stroke-width="1">
              <circle cx="8" cy="8" r="6.5"/>
              <ellipse cx="8" cy="8" rx="3" ry="6.5"/>
              <line x1="1.5" y1="8" x2="14.5" y2="8"/>
              <line x1="2.5" y1="5" x2="13.5" y2="5"/>
              <line x1="2.5" y1="11" x2="13.5" y2="11"/>
            </g>
          </svg>
          <span>www.dorvak-example.nl</span>
        </li>
      </ul>
    </div>
  </section>
</body>
</html>
```